Medida Certa - Working hours register App needs interface design

Medida Certa, a 1 million users Brazilian website focused on general calculations needs an interface to an App for registering the working hours of a housemaid, a nanny, a housekeeper or other domestic workers.
The final users should be mainly housewifes.
The wireframe of the pages is in the LarPonto_layout.xls file attached.
Logo is also available in the wireframe.
The interface should be optimized for Android on Orbita KX with a 5'' screen.
Target Market(s)
Females, educated, from 30 to 50 y.o.
Industry/Entity Type
Android
Look and feel
Each slider illustrates characteristics of the customer's brand and the style your logo design should communicate.

```html
<!DOCTYPE html>
<html lang="pt">
<head>
<meta charset="utf-8">
<title>Medida Certa – Registro de Horas</title>
<link rel="stylesheet" href="https://fonts.googleapis.com/css2?family=Arimo:wght@400;700&display=swap">
<style>
:root{
  --page:#f2f2f2;
  --brand-red:#c4000a;
  --header-dark:#2a0a0a;
  --header-mid:#5a1414;
  --row-a:#d9d9d9;
  --row-b:#ebebeb;
  --text:#333333;
  --white:#ffffff;
  --btn-grey:#d2d2d2;
  --btn-green:#5cbf3c;
  --panel-dark:#474747;
  --panel-light:#7a7a7a;
  --side-red:#8e2525;
  --sheet:#ececec;
  --cell:#dcdcdc;
}
*{box-sizing:border-box;margin:0;padding:0}
html,body{width:1200px;height:1000px;overflow:hidden;background:var(--page);font-family:"Arimo",Arial,sans-serif;color:var(--text)}
.screen{position:absolute;top:108px;width:434px;height:760px;overflow:hidden;background:var(--sheet);box-shadow:0 2px 10px rgba(0,0,0,.25)}
.screen--list{left:62px}
.screen--register{left:674px}
.app-header{position:absolute;left:0;top:0;width:100%;height:68px;background:linear-gradient(90deg,var(--header-mid),var(--header-dark) 60%,#1a0606);border-bottom:2px solid #fff}
.brand-mark{position:absolute;left:6px;top:6px;width:66px;height:56px;background:var(--brand-red);border-radius:6px}
.brand-name{position:absolute;right:12px;top:14px;font-size:34px;font-weight:700;color:var(--white)}
.brand-tag{position:absolute;right:14px;top:48px;font-size:12px;color:var(--white)}
.app-footer{position:absolute;left:0;top:692px;width:100%;height:68px;background:linear-gradient(90deg,#3a0c0c,var(--header-dark) 50%,#3a0c0c);border-top:2px solid #fff}
/* list */
.worker{position:absolute;left:0;width:100%;height:124px}
.worker:nth-child(odd){background:var(--row-a)}
.worker:nth-child(even){background:var(--row-b)}
.worker__photo{position:absolute;left:12px;top:24px;width:78px;height:76px;border:2px solid #fff;box-shadow:0 1px 3px rgba(0,0,0,.4)}
.worker__name{position:absolute;left:121px;top:53px;font-size:17px}
.icon-btn{position:absolute;width:48px;height:46px;border-radius:6px;background:linear-gradient(#f4f4f4,#cfcfcf);border:1px solid #aaa;display:flex;align-items:center;justify-content:center}
.worker .icon-btn--keys{left:376px;top:8px}
.worker .icon-btn--edit{left:376px;top:68px}
.photo-placeholder{background:#111;color:#fff;text-align:center;font-size:12px;line-height:1;display:flex;flex-direction:column;justify-content:center}
.photo-placeholder b{font-size:15px;font-weight:400}
.nav-btn{position:absolute;top:10px;width:106px;height:46px;border-radius:4px;display:flex;align-items:center;justify-content:center;text-align:center;font-size:16px;color:#555;background:linear-gradient(#eeeeee,var(--btn-grey))}
.nav-btn--data{left:16px}
.nav-btn--new{left:164px;color:#fff;font-weight:700;font-size:14px;line-height:1.2;background:linear-gradient(#7ed35a,var(--btn-green))}
.nav-btn--config{left:310px}
/* register */
.section-title{position:absolute;left:0;top:70px;width:100%;height:28px;background:linear-gradient(#8a8a8a,#666);color:#fff;font-weight:700;font-size:22px;padding-left:10px;line-height:28px;border-bottom:2px solid #fff}
.profile{position:absolute;left:0;top:98px;width:100%;height:170px;background:linear-gradient(90deg,#5a5a5a,#bdbdbd 30%,#555 40%)}
.profile__photo{position:absolute;left:16px;top:34px;width:96px;height:94px;border:3px solid #fff}
.profile__field{position:absolute;left:116px;width:318px;color:#fff;font-size:22px;padding-left:32px;display:flex;align-items:center}
.side-band{position:absolute;left:0;top:268px;width:122px;height:424px;background:linear-gradient(#c05050,var(--side-red) 35%,#6a1c1c)}
.sheet{position:absolute;left:122px;top:268px;width:312px;height:424px;background:linear-gradient(90deg,#fafafa,#e2e2e2)}
.line{position:absolute;left:12px;width:296px;height:17px;font-size:13px;display:flex;justify-content:space-between;padding:0 30px 0 6px;line-height:17px}
.line--shade{background:var(--cell)}
.heading{position:absolute;left:18px;font-size:13px;font-weight:700;text-decoration:underline}
.choice{position:absolute;left:18px;font-size:13px}
.choice .pick{background:#d0d0d0;padding:1px 4px;border-radius:2px}
.choice .opts{position:absolute;left:94px;white-space:nowrap}
.icon-btn--home{left:10px;top:10px}
.icon-btn--pencil{left:376px;top:10px}
</style>
</head>
<body>

<svg width="0" height="0" style="position:absolute">
  <defs>
    <symbol id="i-keys" viewBox="0 0 40 30"><rect x="2" y="4" width="36" height="22" rx="4" fill="none" stroke="#444" stroke-width="2.5" transform="rotate(-20 20 15)"/><g fill="#444" transform="rotate(-20 20 15)"><rect x="7" y="9" width="4" height="3"/><rect x="13" y="9" width="4" height="3"/><rect x="19" y="9" width="4" height="3"/><rect x="25" y="9" width="4" height="3"/><rect x="7" y="14" width="4" height="3"/><rect x="13" y="14" width="4" height="3"/><rect x="19" y="14" width="4" height="3"/><rect x="25" y="14" width="4" height="3"/><rect x="11" y="19" width="16" height="3"/></g></symbol>
    <symbol id="i-pencil" viewBox="0 0 40 40"><path d="M28 4l8 8L14 34l-10 2 2-10z" fill="none" stroke="#444" stroke-width="3" stroke-linejoin="round"/><path d="M24 8l8 8" stroke="#444" stroke-width="3"/></symbol>
    <symbol id="i-home" viewBox="0 0 40 40"><path d="M4 20L20 6l16 14" fill="none" stroke="#222" stroke-width="4"/><path d="M9 18v18h8V26h6v10h8V18L20 9z" fill="#222"/></symbol>
  </defs>
</svg>

<section class="screen screen--list">
  <header class="app-header">
    <span class="brand-mark"></span>
    <span class="brand-name">Medida Certa</span>
    <span class="brand-tag">Aplicação mobile</span>
  </header>
  <div style="position:absolute;left:0;top:70px;width:100%">
    <article class="worker" style="top:0">
      <div class="worker__photo" role="img" aria-label="Foto da empregada" style="background:linear-gradient(#8a8a8a,#3a3a3a)"></div>
      <span class="worker__name">1. Marta Ribeiro de Souza</span>
      <span class="icon-btn icon-btn--keys"><svg width="34" height="28"><use href="#i-keys"/></svg></span>
      <span class="icon-btn icon-btn--edit"><svg width="30" height="30"><use href="#i-pencil"/></svg></span>
    </article>
    <article class="worker" style="top:124px">
      <div class="worker__photo" role="img" aria-label="Foto da empregada" style="background:linear-gradient(#a0552a,#d89a6a)"></div>
      <span class="worker__name">1. Empregada numero dois.</span>
      <span class="icon-btn icon-btn--keys"><svg width="34" height="28"><use href="#i-keys"/></svg></span>
      <span class="icon-btn icon-btn--edit"><svg width="30" height="30"><use href="#i-pencil"/></svg></span>
    </article>
    <article class="worker" style="top:248px">
      <div class="worker__photo" role="img" aria-label="Foto da empregada" style="background:linear-gradient(90deg,#ffffff,#555 50%,#ffffff)"></div>
      <span class="worker__name">1. Empregada numero três</span>
      <span class="icon-btn icon-btn--keys"><svg width="34" height="28"><use href="#i-keys"/></svg></span>
      <span class="icon-btn icon-btn--edit"><svg width="30" height="30"><use href="#i-pencil"/></svg></span>
    </article>
    <article class="worker" style="top:372px">
      <div class="worker__photo" role="img" aria-label="Foto da empregada" style="background:linear-gradient(#d8b878,#e6c6a8 60%,#b0bcc8)"></div>
      <span class="worker__name">1. Empregada numero quatro</span>
      <span class="icon-btn icon-btn--keys"><svg width="34" height="28"><use href="#i-keys"/></svg></span>
      <span class="icon-btn icon-btn--edit"><svg width="30" height="30"><use href="#i-pencil"/></svg></span>
    </article>
    <article class="worker" style="top:496px">
      <div class="worker__photo photo-placeholder" role="img" aria-label="Espaço para foto"><b>Click</b>to add<br>PHOTO</div>
      <span class="worker__name">1. Empregada numero cinco</span>
      <span class="icon-btn icon-btn--keys"><svg width="34" height="28"><use href="#i-keys"/></svg></span>
      <span class="icon-btn icon-btn--edit"><svg width="30" height="30"><use href="#i-pencil"/></svg></span>
    </article>
  </div>
  <footer class="app-footer">
    <span class="nav-btn nav-btn--data">My Data</span>
    <span class="nav-btn nav-btn--new">Nova<br>Empregada</span>
    <span class="nav-btn nav-btn--config">Configuration</span>
  </footer>
</section>

<section class="screen screen--register">
  <header class="app-header">
    <span class="brand-mark"></span>
    <span class="brand-name">Medida Certa</span>
    <span class="brand-tag">Aplicação mobile</span>
  </header>
  <h2 class="section-title">Employee Registration</h2>
  <div class="profile">
    <div class="profile__photo photo-placeholder" role="img" aria-label="Espaço para foto" style="background:linear-gradient(90deg,#eee,#111 40%,#111 70%,#eee)"><b>Click</b>to add<br>PHOTO</div>
    <div class="profile__field" style="top:0;height:60px;background:var(--panel-dark)">Add Name</div>
    <div class="profile__field" style="top:60px;height:58px;background:var(--panel-light)">Add NickName</div>
    <div class="profile__field" style="top:118px;height:52px;background:var(--panel-dark)">Add Date</div>
  </div>
  <div class="side-band"></div>
  <div class="sheet">
    <div class="line" style="top:14px"><span>Date</span><span>25 de Janeiro 2013</span></div>
    <div class="line line--shade" style="top:31px"><span>Week Day</span><span></span></div>
    <div class="line" style="top:48px"><span>Arrival</span><span>09:00</span></div>
    <div class="line line--shade" style="top:65px"><span>Lunch Break Start</span><span>12:00</span></div>
    <div class="line" style="top:82px"><span>Lunch Break End</span><span>12:30</span></div>
    <div class="line line--shade" style="top:99px"><span>Out</span><span>17:30</span></div>
    <div class="choice" style="top:150px">Holiday<span class="opts"><span class="pick">Yes</span> / No</span></div>
    <div class="choice" style="top:195px">Absent<span class="opts">Yes / <span class="pick">No</span></span></div>
    <div class="heading" style="top:226px">Day Balance</div>
    <div class="line line--shade" style="top:260px"><span>Working Hours</span><span>08:00</span></div>
    <div class="line" style="top:277px"><span>Intervalo</span><span>00:30</span></div>
    <div class="line line--shade" style="top:294px"><span>Extra Hours</span><span>00:00</span></div>
    <div class="line" style="top:311px"><span>Night Extra Hours</span><span>00:00</span></div>
    <div class="line line--shade" style="top:328px"><span>Hour Balance</span><span>00:00</span></div>
    <div class="heading" style="top:366px">Employe Monthly Report</div>
    <div class="line line--shade" style="top:399px"><span>Working Hours</span><span>08:00</span></div>
    <div class="line" style="top:416px"><span>Compensated Hour</span><span>00:30</span></div>
  </div>
  <footer class="app-footer">
    <span class="icon-btn icon-btn--home"><svg width="32" height="32"><use href="#i-home"/></svg></span>
    <span class="icon-btn icon-btn--pencil"><svg width="30" height="30"><use href="#i-pencil"/></svg></span>
  </footer>
</section>

</body>
</html>
```